Our Work

I would like to Upload Pictures and make a flyer showing some of the services we offer. I have attached a sample flyer layout and pictures I would like to use with the services labeled.

```html
<!DOCTYPE html>
<html lang="en">
<head>
<meta charset="utf-8">
<title>Kalveris Contracting Flyer</title>
<link rel="stylesheet" href="https://fonts.googleapis.com/css2?family=Montserrat:wght@500;600;700;800;900&display=swap">
<style>
  :root {
    --bg: #e4e2de;
    --paper: #f4f5f7;
    --navy: #1f1d6b;
    --yellow: #f2c12e;
    --lavender: #a7a4d6;
    --ink: #22223a;
    --purple: #4a3a9e;
    --dark: #3a3a3c;
  }
  * { box-sizing: border-box; margin: 0; padding: 0; }
  html, body { width: 1168px; height: 1200px; overflow: hidden; background: var(--bg); }
  body { font-family: "Montserrat", sans-serif; position: relative; }

  .flyer {
    position: absolute; left: 164px; top: 20px; width: 840px; height: 1160px;
    background: var(--paper); overflow: hidden;
    box-shadow: 0 6px 20px rgba(0,0,0,.18);
  }

  .header { position: absolute; left: 0; top: 0; width: 100%; height: 200px; background: #f3f4f6; }
  .floorplan {
    position: absolute; right: 0; top: 0; width: 420px; height: 200px;
    background: linear-gradient(135deg, #eef0f3 0%, #e3e6ea 60%, #eceef1 100%);
  }
  .brand {
    position: absolute; left: 58px; top: 42px; width: 300px; height: 120px;
    background: #ffffff; display: flex; align-items: center; justify-content: center; gap: 12px;
  }
  .brand-mark { width: 14px; height: 14px; background: var(--yellow); }
  .brand-name { font-weight: 800; color: var(--navy); font-size: 25px; line-height: 1.15; letter-spacing: 1px; text-align: left; }
  .header-url {
    position: absolute; right: 44px; top: 150px; font-weight: 700; font-size: 15px; color: var(--navy);
  }

  .hero {
    position: absolute; left: 0; top: 200px; width: 100%; height: 410px;
    background: linear-gradient(160deg, #505052 0%, #3a3a3c 45%, #2c2c2e 100%);
  }
  .title { position: absolute; left: 60px; top: 290px; color: #fff; font-weight: 900; font-size: 104px; letter-spacing: -2px; line-height: 1; }
  .subtitle { position: absolute; left: 62px; top: 400px; color: var(--yellow); font-weight: 800; font-size: 52px; line-height: 1; letter-spacing: -0.5px; }
  .title-rule { position: absolute; left: 62px; top: 470px; width: 696px; height: 4px; background: var(--yellow); }

  .gallery { position: absolute; left: 56px; top: 528px; display: flex; gap: 8px; }
  .gallery-frame { width: 236px; height: 224px; border: 3px solid var(--yellow); padding: 6px; background: transparent; }
  .gallery-photo { width: 100%; height: 100%; }
  .photo-1 { background: linear-gradient(160deg, #8d8f96 0%, #a89a86 50%, #6e6f76 100%); }
  .photo-2 { background: linear-gradient(180deg, #3f6fb8 0%, #b8bcc2 45%, #a5503a 75%, #4d6b3c 100%); }
  .photo-3 { background: linear-gradient(170deg, #6b4a36 0%, #c8c6c0 45%, #6e7f95 100%); }

  .services-title {
    position: absolute; left: 58px; top: 778px; width: 740px;
    color: var(--lavender); font-weight: 900; font-size: 43px; letter-spacing: -0.5px; white-space: nowrap;
  }
  .services { position: absolute; left: 58px; top: 838px; display: flex; gap: 20px; }
  .services ul { list-style: none; }
  .services li { font-size: 16.5px; font-weight: 500; color: var(--ink); line-height: 21px; padding-left: 20px; position: relative; white-space: nowrap; }
  .services li::before { content: ""; position: absolute; left: 4px; top: 9px; width: 5px; height: 5px; border-radius: 50%; background: var(--ink); }
  .col-a { width: 290px; }
  .col-b { width: 210px; }
  .col-c { width: 220px; }

  .footer {
    position: absolute; left: 0; top: 1010px; width: 100%; height: 150px;
    background: linear-gradient(90deg, #3d2f94 0%, #5a45a8 35%, #b99a5e 58%, #f1c828 72%, #f3cc25 100%);
  }
  .perks { position: absolute; left: 56px; top: 42px; list-style: none; }
  .perks li { color: #fff; font-weight: 800; font-size: 15.5px; line-height: 21px; text-transform: uppercase; display: flex; align-items: flex-start; gap: 8px; white-space: nowrap; }
  .perks li svg { width: 20px; height: 18px; flex: none; margin-top: 1px; }
  .perks li.cont { padding-left: 28px; }
  .contact { position: absolute; left: 494px; top: 50px; color: var(--ink); }
  .contact-web { font-weight: 700; font-size: 20px; }
  .contact-phone { font-weight: 700; font-size: 37px; line-height: 1.1; letter-spacing: -0.5px; }
  .contact-mail { font-weight: 700; font-size: 20px; }
</style>
</head>
<body>
  <main class="flyer">
    <header class="header">
      <div class="floorplan" role="img" aria-label="Faint architectural floor plan drawing"></div>
      <div class="brand">
        <span class="brand-mark"></span>
        <span class="brand-name">KALVERIS<br>CONTRACTING</span>
      </div>
      <div class="header-url">www.kalveriscontracting.com</div>
    </header>

    <section class="hero" role="img" aria-label="Interior renovation with workers on scaffolding, dark tinted photo"></section>
    <h1 class="title">KALVERIS</h1>
    <h2 class="subtitle">CONTRACTING</h2>
    <div class="title-rule"></div>

    <div class="gallery">
      <div class="gallery-frame"><div class="gallery-photo photo-1" role="img" aria-label="Workers on ladders repairing exterior siding"></div></div>
      <div class="gallery-frame"><div class="gallery-photo photo-2" role="img" aria-label="Brick townhouse exterior under renovation"></div></div>
      <div class="gallery-frame"><div class="gallery-photo photo-3" role="img" aria-label="Crew installing a sliding patio door"></div></div>
    </div>

    <h3 class="services-title">EXTERIOR &amp; INTERIOR PAINTING</h3>
    <div class="services">
      <ul class="col-a">
        <li>General Carpentry</li>
        <li>Framing Repairs</li>
        <li>Siding/Gutters/Windows/Doors</li>
        <li>Concrete Walkways/Stoops</li>
        <li>Balcony/Deck Rehab</li>
        <li>Tuckpointing</li>
        <li>Sealants/Caulks</li>
      </ul>
      <ul class="col-b">
        <li>Pressure Washing</li>
        <li>Specialty Coatings</li>
        <li>Drywall Install/Repair</li>
        <li>Plaster Repairs</li>
        <li>Wallpaper Removal</li>
        <li>Flooring/Tile/Carpet</li>
        <li>Harhwood/Vinyl</li>
      </ul>
      <ul class="col-c">
        <li>Leak Investigations:</li>
        <li>Facades, Roofs,</li>
        <li>Interior Leaks</li>
        <li>EIFS/Stucco Repairs</li>
        <li>Plumbing Repairs</li>
        <li>Roofing Repairs</li>
        <li>Lead Safe Renovations</li>
      </ul>
    </div>

    <footer class="footer">
      <ul class="perks">
        <li><svg viewBox="0 0 20 18"><path d="M2 9 L8 15 L18 2" fill="none" stroke="#fff" stroke-width="3"/></svg>Quick Estimates</li>
        <li><svg viewBox="0 0 20 18"><path d="M2 9 L8 15 L18 2" fill="none" stroke="#fff" stroke-width="3"/></svg>Yearly Maintenance Contracts</li>
        <li><svg viewBox="0 0 20 18"><path d="M2 9 L8 15 L18 2" fill="none" stroke="#fff" stroke-width="3"/></svg>Fast Response to General Services</li>
        <li class="cont">Work Order Repairs, Guaranteed!!!</li>
      </ul>
      <div class="contact">
        <div class="contact-web">kalveriscontracting.com</div>
        <div class="contact-phone">555.014.0172</div>
        <div class="contact-mail">info@kalveriscontracting.com</div>
      </div>
    </footer>
  </main>
</body>
</html>
```